" A Voltrana é uma empresa cuja especialidade é atuar diretamente no setor de energia, oferecendo a seus clientes gestão de energia e utilidades (água, gás, vapor, ar comprimido) com o objetivo principal de obter informações, padrões e variáveis de consumo e também eficiência energética para agir de forma assertiva no foco do desperdício e na otimização da utilização dos recursos em um parque industrial ou edifício. "

```html
<!DOCTYPE html>
<html lang="pt-BR">
<head>
<meta charset="UTF-8">
<title>Voltrana – Envelopes e CDs</title>
<link href="https://fonts.googleapis.com/css2?family=Montserrat:wght@400;600&display=swap" rel="stylesheet">
<style>
  :root {
    --bg: #e9e9e9;
    --bg-center: #f6f6f6;
    --green: #1f9a43;
    --green-soft: #26a84b;
    --yellow: #f5b21c;
    --yellow-soft: #f8bf33;
    --white: #ffffff;
    --hub: #6f6f6f;
    --hub-ring: #d9d9d9;
  }
  html, body {
    margin: 0;
    width: 1200px;
    height: 1200px;
    overflow: hidden;
  }
  body {
    background: radial-gradient(circle at 50% 50%, var(--bg-center) 0%, var(--bg) 70%);
    font-family: "Montserrat", sans-serif;
    position: relative;
  }
  .envelope {
    position: absolute;
  }
  .envelope--green { left: 163px; top: 180px; width: 377px; height: 480px; }
  .envelope--yellow { left: 665px; top: 528px; width: 377px; height: 444px; }
  .envelope__flap {
    position: absolute;
    left: -10px; top: 0;
    width: calc(100% + 20px);
    height: 26px;
  }
  .envelope__body {
    position: absolute;
    left: 0; top: 24px; right: 0; bottom: 0;
    box-shadow: 0 4px 10px rgba(0,0,0,0.18);
  }
  .envelope--green .envelope__body {
    background: linear-gradient(160deg, var(--green-soft) 0%, var(--green) 100%);
  }
  .envelope--yellow .envelope__body {
    background: linear-gradient(160deg, var(--yellow-soft) 0%, var(--yellow) 100%);
  }
  .brand {
    position: absolute;
    left: 0; width: 100%;
    text-align: center;
    color: var(--white);
  }
  .envelope--green .brand { top: 218px; }
  .envelope--yellow .brand { top: 180px; }
  .brand__mark {
    display: block;
    width: 42px; height: 42px;
    margin: 0 auto 14px;
    border-radius: 50%;
    background: var(--white);
  }
  .brand__name {
    display: block;
    font-weight: 600;
    font-size: 40px;
    letter-spacing: 1px;
    line-height: 1;
  }
  .brand__tagline {
    display: block;
    font-weight: 400;
    font-size: 15px;
    letter-spacing: 2px;
    margin-top: 5px;
  }
  .disc {
    position: absolute;
    filter: drop-shadow(0 4px 8px rgba(0,0,0,0.22));
  }
  .disc--left { left: 162px; top: 620px; width: 340px; height: 340px; }
  .disc--right { left: 667px; top: 228px; width: 372px; height: 372px; }
  .disc__name { font-family: "Montserrat", sans-serif; font-weight: 600; fill: var(--green); }
  .disc__tagline { font-family: "Montserrat", sans-serif; font-weight: 400; fill: var(--green); }
</style>
</head>
<body>

  <section class="envelope envelope--green">
    <div class="envelope__body" role="img" aria-label="Fundo verde com padrão de pequenas marcas repetidas"></div>
    <svg class="envelope__flap" viewBox="0 0 397 26" preserveAspectRatio="none" aria-hidden="true">
      <polygon points="0,0 397,0 387,26 10,26" fill="#f5b21c"/>
    </svg>
    <div class="brand">
      <span class="brand__mark"></span>
      <span class="brand__name">VOLTRANA</span>
      <span class="brand__tagline">Soluções em Energia</span>
    </div>
  </section>

  <section class="envelope envelope--yellow">
    <div class="envelope__body" role="img" aria-label="Fundo amarelo com padrão de pequenas marcas repetidas"></div>
    <svg class="envelope__flap" viewBox="0 0 397 26" preserveAspectRatio="none" aria-hidden="true">
      <polygon points="0,0 397,0 387,26 10,26" fill="#1f9a43"/>
    </svg>
    <div class="brand">
      <span class="brand__mark"></span>
      <span class="brand__name">VOLTRANA</span>
      <span class="brand__tagline">Soluções em Energia</span>
    </div>
  </section>

  <svg class="disc disc--left" viewBox="0 0 200 200" aria-label="CD Voltrana">
    <defs>
      <clipPath id="disc-clip-a"><circle cx="100" cy="100" r="100"/></clipPath>
      <linearGradient id="disc-art-a" x1="0" y1="0" x2="0" y2="1">
        <stop offset="0" stop-color="#1f9a43"/>
        <stop offset="0.55" stop-color="#1f9a43"/>
        <stop offset="1" stop-color="#f5b21c"/>
      </linearGradient>
    </defs>
    <g clip-path="url(#disc-clip-a)">
      <rect width="200" height="200" fill="#ffffff"/>
      <rect x="0" y="45" width="200" height="155" fill="url(#disc-art-a)" role="img" aria-label="Faixa decorativa da marca em verde e amarelo"/>
      <line x1="60" y1="168" x2="145" y2="168" stroke="#fbe0a0" stroke-width="1"/>
      <line x1="55" y1="180" x2="150" y2="180" stroke="#fbe0a0" stroke-width="1"/>
    </g>
    <circle cx="100" cy="100" r="22" fill="#d9d9d9"/>
    <circle cx="100" cy="100" r="19" fill="#6f6f6f"/>
    <circle cx="47" cy="26" r="4" fill="#f5b21c"/>
    <text class="disc__name" x="54" y="30" font-size="11">VOLTRANA</text>
    <text class="disc__tagline" x="55" y="37" font-size="4.5">Soluções em Energia</text>
  </svg>

  <svg class="disc disc--right" viewBox="0 0 200 200" aria-label="CD Voltrana">
    <defs>
      <clipPath id="disc-clip-b"><circle cx="100" cy="100" r="100"/></clipPath>
      <linearGradient id="disc-art-b" x1="0" y1="0" x2="0" y2="1">
        <stop offset="0" stop-color="#1f9a43"/>
        <stop offset="0.55" stop-color="#1f9a43"/>
        <stop offset="1" stop-color="#f5b21c"/>
      </linearGradient>
    </defs>
    <g clip-path="url(#disc-clip-b)">
      <rect width="200" height="200" fill="#ffffff"/>
      <rect x="0" y="55" width="200" height="145" fill="url(#disc-art-b)" role="img" aria-label="Faixa decorativa da marca em verde e amarelo"/>
      <line x1="60" y1="170" x2="145" y2="170" stroke="#fbe0a0" stroke-width="1"/>
      <line x1="55" y1="182" x2="150" y2="182" stroke="#fbe0a0" stroke-width="1"/>
    </g>
    <circle cx="100" cy="100" r="22" fill="#d9d9d9"/>
    <circle cx="100" cy="100" r="19" fill="#6f6f6f"/>
    <circle cx="62" cy="27" r="4" fill="#f5b21c"/>
    <text class="disc__name" x="69" y="31" font-size="12">VOLTRANA</text>
    <text class="disc__tagline" x="70" y="38" font-size="4.5">Soluções em Energia</text>
  </svg>

</body>
</html>
```